KRW Brochure

I would like to update our brochure and add additional services as well as change our logo, We are a full service PEO and a full service Payroll company
Target Market(s)
Business to Business
Industry/Entity Type
Payroll and Benefits
Font styles to use
Sans Serif

```html
<!DOCTYPE html>
<html lang="en">
<head>
<meta charset="utf-8">
<title>KRW Brochure</title>
<link rel="stylesheet" href="https://fonts.googleapis.com/css2?family=Cinzel:wght@700;900&family=Great+Vibes&family=Open+Sans:wght@400;600;700&display=swap">
<style>
:root{
  --maroon:#6b1420;
  --maroon-dark:#4a0c15;
  --gold:#c9a13b;
  --gold-light:#e6c97a;
  --ink:#333;
  --backdrop:#d9d9d9;
  --photo-a:#8a6a4a;
  --photo-b:#c9b08a;
}
*{box-sizing:border-box;margin:0;padding:0}
html,body{width:1200px;height:3084px;overflow:hidden;background:var(--backdrop);font-family:"Open Sans",sans-serif;color:var(--ink)}
.spread{position:absolute;left:50px;display:flex;gap:20px}
.spread-1{top:150px}.spread-2{top:1100px}.spread-3{top:2050px}
.page{position:relative;width:540px;height:790px;background:#fff;overflow:hidden;box-shadow:0 4px 14px rgba(0,0,0,.25)}
.page-footer{position:absolute;left:0;right:0;bottom:0;height:34px;display:flex;justify-content:space-between;align-items:center;padding:0 26px;font-size:11px;font-weight:700;color:var(--maroon);border-top:3px solid var(--gold);background:#fff}
.page-number{background:var(--maroon);color:#fff;padding:3px 10px}
.section-bar{display:flex;align-items:center;background:var(--maroon);color:#fff;font-family:"Cinzel",serif;font-size:14px;font-weight:700;padding:6px 14px;margin:10px 0 8px;border-left:8px solid var(--gold)}
.section-bar:first-child{margin-top:0}
.content{position:absolute;left:26px;right:26px;top:22px;bottom:48px}
p{font-size:9px;line-height:1.55;margin-bottom:6px;text-align:justify}
h4{font-size:10px;color:var(--maroon);font-weight:700;margin:8px 0 2px}
.photo{background:linear-gradient(135deg,var(--photo-a),var(--photo-b))}
.photo-circle{position:absolute;border-radius:50%;border:5px solid var(--gold);background:linear-gradient(135deg,var(--photo-a),var(--photo-b))}
.bullets{font-size:9px;line-height:1.65;padding-left:14px}
.logo{display:flex;align-items:center;gap:8px}
.logo-dot{width:46px;height:46px;border-radius:50%;background:var(--maroon)}
.logo-name{font-family:"Cinzel",serif;font-weight:900;color:var(--maroon);font-size:40px;line-height:1}
.two-col{display:flex;gap:14px;margin:4px 0 6px}
.two-col>*{flex:1}
/* cover */
.cover-shapes,.cover-collage{position:absolute;left:0;top:0}
.cover-title-block{position:absolute;left:0;right:0;top:178px;text-align:center}
.welcome{font-family:"Great Vibes",cursive;color:var(--gold-light);font-size:46px;line-height:1}
.cover-title{font-family:"Cinzel",serif;font-weight:900;color:#fff;font-size:34px;line-height:1.1;margin-top:4px}
.cover-bottom{position:absolute;left:34px;right:30px;top:640px;display:flex;align-items:center;gap:22px}
.tagline{font-size:14px;color:var(--maroon);font-weight:600;line-height:1.4}
/* page 1 */
.page-one-header{position:absolute;left:0;top:0}
.page-one .content{top:120px}
.stats{display:flex;gap:10px;margin:8px 0}
.stat{flex:1;background:var(--gold);color:var(--maroon-dark);text-align:center;font-size:9.5px;font-weight:700;padding:9px 4px}
/* back */
.back-shapes{position:absolute;left:0;top:0}
.back-logo{position:absolute;left:0;right:0;top:250px;justify-content:center}
.back-logo .logo-dot{width:84px;height:84px}
.back-logo .logo-name{font-size:78px}
.back-name{position:absolute;left:0;right:0;top:355px;text-align:center;font-family:"Cinzel",serif;color:var(--maroon);font-size:18px;font-weight:700}
.back-tagline{position:absolute;left:0;right:0;top:384px;text-align:center;font-size:10px;color:var(--gold);font-weight:600}
.back-contact{position:absolute;right:30px;top:600px;text-align:right;font-size:10px;line-height:1.6;color:var(--maroon);font-weight:600;font-style:normal}
</style>
</head>
<body>

<section class="spread spread-1">
  <article class="page cover">
    <svg class="cover-shapes" width="540" height="790" viewBox="0 0 540 790" aria-hidden="true">
      <path d="M0 150 Q270 95 540 150 L540 365 Q270 325 0 365 Z" fill="var(--maroon)"/>
      <path d="M0 142 Q270 87 540 142" fill="none" stroke="var(--gold)" stroke-width="5"/>
      <path d="M0 374 Q270 334 540 374" fill="none" stroke="var(--gold)" stroke-width="5"/>
      <path d="M0 590 Q270 650 540 585" fill="none" stroke="var(--gold)" stroke-width="6"/>
      <path d="M0 604 Q270 664 540 599" fill="none" stroke="var(--maroon)" stroke-width="3"/>
    </svg>
    <svg class="cover-collage" width="540" height="790" viewBox="0 0 540 790" role="img" aria-label="Collage of office workers, payroll documents and a hard hat">
      <defs><linearGradient id="collage" x1="0" y1="0" x2="1" y2="1"><stop offset="0" stop-color="#8a6a4a"/><stop offset="1" stop-color="#c9b08a"/></linearGradient></defs>
      <path d="M0 380 Q270 340 540 380 L540 580 Q270 640 0 584 Z" fill="url(#collage)"/>
    </svg>
    <div class="photo-circle" style="left:34px;top:8px;width:140px;height:140px" role="img" aria-label="Stack of coins and cash"></div>
    <div class="cover-title-block">
      <div class="welcome">Welcome to</div>
      <h1 class="cover-title">KEYSTONE RESOURCE<br>WORKS</h1>
    </div>
    <div class="cover-bottom">
      <div class="logo"><span class="logo-dot"></span><span class="logo-name">KRW</span></div>
      <div class="tagline">We are ready to provide you with the benefit management services you need!</div>
    </div>
    <footer class="page-footer"><span>www.krwpayroll.example</span></footer>
  </article>

  <article class="page page-one">
    <svg class="page-one-header" width="540" height="120" viewBox="0 0 540 120" aria-hidden="true">
      <path d="M0 0 H540 V70 Q270 110 0 70 Z" fill="var(--maroon)"/>
      <path d="M0 78 Q270 118 540 78" fill="none" stroke="var(--gold)" stroke-width="4"/>
    </svg>
    <div class="photo-circle" style="left:330px;top:8px;width:92px;height:92px" role="img" aria-label="Business people at a meeting"></div>
    <div class="photo-circle" style="left:430px;top:8px;width:92px;height:92px" role="img" aria-label="Human resources team at work"></div>
    <div class="content">
      <div class="section-bar">About KRW and Key Employment Statistics</div>
      <p>Since our founding, we have helped small and midsize firms manage payroll, benefits and compliance so owners can focus on growth. Our team handles the details that keep staff paid on time and covered by quality plans, and we treat every client like a partner rather than an account number.</p>
      <p>As a full service PEO and payroll provider, we pool the buying power of many clients to offer rates once reserved for large employers. We also track changing rules so your company stays current and protected. From the first paycheck to the annual audit, our specialists stand beside you with clear answers and practical tools.</p>
      <p>Our clients range from family shops with a handful of workers to growing firms with several hundred staff across many states. Each one receives a dedicated service contact, a secure online portal and access to our full bench of payroll, benefits, tax and human resources experts.</p>
      <p>We believe a strong workforce begins with trust. That is why we keep our pricing simple, our reporting open and our team easy to reach by phone, email or video whenever you need help with a question large or small.</p>
      <div class="section-bar">Key Statistics</div>
      <p>Independent studies show that firms working with a PEO grow faster, keep staff longer and are far less likely to close in hard times. The figures below show typical results reported by small and midsize employers who share duties with a PEO.</p>
      <div class="stats">
        <div class="stat">Growth 9% faster</div>
        <div class="stat">Turnover 12% lower</div>
        <div class="stat">Savings $450 per staff</div>
      </div>
      <p>As shown above, a business can save time and money when payroll, benefits and compliance move to one trusted partner. Owners report more hours each week for sales, service and planning, and staff report higher satisfaction with their benefits.</p>
      <p>Results vary by size and industry, yet most clients see clear gains within their first year with us. Contact our team for a free review of your current costs and a plan built around your goals.</p>
    </div>
    <footer class="page-footer"><span>www.krwpayroll.example</span><span class="page-number">Page 01</span></footer>
  </article>
</section>

<section class="spread spread-2">
  <article class="page">
    <div class="content">
      <div class="section-bar">KRW Mission</div>
      <p>Our mission is to give every client the service, tools and support of a large human resources team at a price that fits a growing business. We measure success by the time we save you and the peace of mind we bring to you and your staff.</p>
      <div class="section-bar">KRW ASO and PEO Services</div>
      <h4>Administrative Services Organization (ASO)</h4>
      <p>Keep full control of your benefits while we run payroll, tax filing and reporting behind the scenes with accuracy and care. An ASO fits firms that wish to keep their own plans and employer status but want expert help with daily tasks, year end forms and changing tax rules across states.</p>
      <p>Our ASO clients receive payroll processing, garnishment handling, new hire reporting and quarterly filings, all backed by our guarantee of on time payment and accurate deposits.</p>
      <h4>Professional Employer Organization (PEO)</h4>
      <p>Share employer duties with us and gain access to group health plans, workers compensation and expert HR guidance. As a co-employer we take on payroll tax liability, unemployment claims and many compliance tasks, while you keep full direction of daily work, hiring and company culture.</p>
      <p>Because we combine many small firms into one large group, our PEO clients enjoy richer plan choices and steadier rates than they could obtain on their own.</p>
      <div class="two-col">
        <ul class="bullets">
          <li>Payroll processing and filing</li>
          <li>Direct deposit and paycards</li>
          <li>Health, dental and vision plans</li>
          <li>Retirement plan options</li>
          <li>Workers compensation</li>
          <li>Unemployment claims handling</li>
          <li>Time and attendance</li>
          <li>Employee handbooks</li>
          <li>Online self service portal</li>
          <li>Benefits enrollment support</li>
          <li>State and federal tax filing</li>
          <li>Year end forms and reports</li>
        </ul>
        <div class="photo" style="height:190px" role="img" aria-label="Hands typing on a laptop with payroll charts"></div>
      </div>
      <p>Not sure which model fits your firm? Our advisors will compare both options side by side and help you choose the path that best serves your budget and your people.</p>
    </div>
    <footer class="page-footer"><span>www.krwpayroll.example</span><span class="page-number">Page 02</span></footer>
  </article>

  <article class="page">
    <div class="content">
      <div class="section-bar">KRW Workforce Services</div>
      <p>Beyond payroll and benefits, we support the people side of your business from hiring through retirement. Each service below may be added to any ASO or PEO plan.</p>
      <h4>Recruiting and Onboarding</h4>
      <p>We post openings, screen candidates and set new hires up with forms, training and pay in a single smooth flow. Electronic onboarding lets new staff sign documents, choose benefits and enter bank details before their first day, so they arrive ready to work.</p>
      <h4>Virtual HR for Compliance and HR Best Practices</h4>
      <p>Certified advisors answer questions, review policies and help you handle hard conversations with confidence. Reach our team by phone or email for guidance on leave, wage and hour rules, terminations and workplace investigations.</p>
      <div class="two-col">
        <div class="photo" style="height:150px" role="img" aria-label="Advisor speaking with a client at a desk"></div>
        <div>
          <h4 style="margin-top:0">Custom HR Policies and Procedures</h4>
          <p>We draft clear policies that match your state rules and your culture, then update them when laws change. Your handbook stays current, consistent and easy for staff to follow.</p>
          <p>Each policy is reviewed by our compliance team and delivered in print and digital form for simple sharing.</p>
        </div>
      </div>
      <h4>Current Employee Handbook</h4>
      <p>A well written handbook sets expectations and protects your firm. We build and maintain a handbook that covers conduct, pay, leave and benefits, with yearly reviews to keep it in line with new laws.</p>
      <h4>Coaching and Problem Solving</h4>
      <p>Our team guides managers through reviews, discipline and conflict so small issues never become large claims. We provide templates, talking points and follow up support for every step.</p>
      <h4>Performance Management</h4>
      <p>Set goals, track progress and reward results with simple review tools inside our online portal. Managers receive reminders, and staff can view feedback and growth plans at any time.</p>
      <h4>Training and Development</h4>
      <p>Give your staff access to a library of online courses on safety, leadership, customer service and software skills, with progress reports that make tracking simple.</p>
    </div>
    <footer class="page-footer"><span>www.krwpayroll.example</span><span class="page-number">Page 03</span></footer>
  </article>
</section>

<section class="spread spread-3">
  <article class="page">
    <div class="content">
      <div class="section-bar">KRW Workforce Services</div>
      <p>Continued services that keep your workplace safe, fair and ready to grow. Each option can be added at any time as your needs change.</p>
      <h4>Employee Counseling and Workplace Advice</h4>
      <p>Staff can reach trained counselors for support with stress, family needs, money concerns and work issues at no extra cost. Confidential help is available by phone day and night, giving your team a trusted place to turn when life gets hard.</p>
      <h4>Background Checks</h4>
      <p>We run criminal, credit, education and driving checks that follow federal and state rules for fair hiring. Results arrive quickly in your portal, along with clear guidance on how to use them in hiring decisions.</p>
      <h4>Safety and Risk Reviews</h4>
      <p>Our experts visit your site, spot hazards and build a plan that lowers claims and protects your people. We also help with written safety programs, accident reports and return to work plans after an injury.</p>
      <h4>Sexual Harassment Prevention Training</h4>
      <p>Online and live sessions help your team meet state training rules and build a respectful workplace. Certificates are stored in your portal for quick proof of completion during audits.</p>
      <h4>Unemployment Claims Management</h4>
      <p>We respond to claims, gather records and represent your firm at hearings so you can stay focused on running the business.</p>
      <div class="photo" style="height:170px;margin-top:8px" role="img" aria-label="Hard hat and safety gear on a work site"></div>
      <p style="margin-top:8px">Ask our team how these services can be bundled with payroll and benefits for one simple monthly fee.</p>
    </div>
    <footer class="page-footer"><span>www.krwpayroll.example</span><span class="page-number">Page 04</span></footer>
  </article>

  <article class="page back-cover">
    <svg class="back-shapes" width="540" height="790" viewBox="0 0 540 790" aria-hidden="true">
      <path d="M0 720 Q270 680 540 720 L540 790 L0 790 Z" fill="var(--maroon)"/>
      <path d="M0 710 Q270 670 540 710" fill="none" stroke="var(--gold)" stroke-width="5"/>
    </svg>
    <div class="back-logo logo"><span class="logo-dot"></span><span class="logo-name">KRW</span></div>
    <div class="back-name">Keystone Resource Works</div>
    <div class="back-tagline">Your Full Service Payroll and PEO Partner</div>
    <address class="back-contact">
      Keystone Resource Works<br>
      120 Market Street, Suite 4<br>
      Riverton, ST 00000<br>
      (555) 010-2040<br>
      www.krwpayroll.example
    </address>
  </article>
</section>

</body>
</html>
```